Retail Product Label mushrooms

We wish to make a 2x3 inch rectangle product label as shown in the PDF. We wish to use the entire space available to make the words and logo as large as possible. We wish the top 1/3rd to be red with the logo inside it. We wish the bottom 2/3rds to be white with the product name inserted. We still need allocations for the barcode weight etc. as shown in the image uploaded.

Target Market(s)

Retail Label

Industry/Entity Type

Fresh Produce mushrooms

Colors
EB3D1F
EC4F4E
F09395
F8D3D4
FCEDEE

Requirements
Must have
• All included
Nice to have
• Shiitake label is best example of what we seek in a rectangle design
Should not have
• You must include all information in the example (weight barcode area, etc.)

```html
<!DOCTYPE html>
<html lang="en">
<head>
<meta charset="utf-8">
<title>Fresh Produce Mushrooms – Retail Label Samples</title>
<link href="https://fonts.googleapis.com/css2?family=Roboto+Condensed:ital,wght@0,300;0,400;0,700;0,900;1,700;1,900&display=swap" rel="stylesheet">
<style>
  :root {
    --board: #d6d6d6;
    --ink: #000000;
    --paper: #ffffff;
    --brand-red: #eb3d1f;
    --brand-red-deep: #c4301b;
    --pill-red: #ec4f4e;
    --heading: #1a1a1a;
  }
  html, body {
    margin: 0;
    padding: 0;
    width: 1200px;
    height: 901px;
    overflow: hidden;
    background: var(--board);
    font-family: "Roboto Condensed", "Arial Narrow", sans-serif;
  }
  .board {
    position: relative;
    width: 1200px;
    height: 901px;
  }
  .sample-title {
    position: absolute;
    top: 78px;
    margin: 0;
    font-weight: 300;
    font-size: 31px;
    color: var(--heading);
    letter-spacing: 0;
  }
  .sample-title--one { left: 126px; }
  .sample-title--two { left: 645px; }
  .label {
    position: absolute;
    top: 144px;
    width: 429px;
    height: 641px;
  }
  .label--one { left: 126px; }
  .label--two { left: 645px; }
  .label text { font-family: "Roboto Condensed", "Arial Narrow", sans-serif; }
  .logo-small { font-weight: 700; fill: var(--paper); }
  .logo-big { font-weight: 900; fill: var(--paper); }
  .logo-sub { font-weight: 400; fill: var(--paper); }
  .fresh { font-weight: 900; font-style: italic; fill: var(--paper); }
  .product-line { font-weight: 700; fill: var(--brand-red); }
  .product-name { font-weight: 900; }
  .product-name--black { fill: var(--ink); }
  .product-name--red { fill: var(--brand-red); }
  .info-strong { font-weight: 700; fill: var(--ink); }
  .info-regular { font-weight: 400; fill: var(--ink); }
  .website { font-weight: 400; fill: var(--ink); }
</style>
</head>
<body>
<main class="board">
  <h2 class="sample-title sample-title--one">SAMPLE 1</h2>
  <h2 class="sample-title sample-title--two">SAMPLE 2</h2>

  <!-- Label option one: curved white panel -->
  <svg class="label label--one" viewBox="0 0 429 641" aria-label="Fresh produce mushrooms label, option one">
    <rect class="label-frame" x="0" y="0" width="427" height="641" fill="var(--ink)"/>
    <rect class="label-field" x="7" y="7" width="413" height="627" fill="var(--brand-red)"/>
    <path class="label-panel" d="M12 343 Q214 431 417 343 L417 626 L12 626 Z" fill="var(--paper)"/>

    <circle class="logo-emblem" cx="214" cy="70" r="28" fill="var(--paper)" role="img" aria-label="Mushroom emblem of the brand"/>
    <text class="logo-small" x="214" y="165" font-size="62" text-anchor="middle" textLength="143" lengthAdjust="spacingAndGlyphs">YOUR</text>
    <text class="logo-big" x="214" y="270" font-size="130" text-anchor="middle" textLength="279" lengthAdjust="spacingAndGlyphs">LOGO</text>
    <text class="logo-sub" x="214" y="330" font-size="63" text-anchor="middle" textLength="282" lengthAdjust="spacingAndGlyphs">GOES HERE</text>

    <rect class="fresh-pill" x="133" y="361" width="161" height="42" rx="21" fill="var(--pill-red)" stroke="var(--paper)" stroke-width="3"/>
    <text class="fresh" x="214" y="396" font-size="38" text-anchor="middle" textLength="116" lengthAdjust="spacingAndGlyphs">FRESH</text>

    <text class="product-line" x="214" y="457" font-size="52" text-anchor="middle" textLength="201" lengthAdjust="spacingAndGlyphs">PRODUCE</text>
    <text class="product-name product-name--black" x="214" y="507" font-size="59" text-anchor="middle" textLength="325" lengthAdjust="spacingAndGlyphs">MUSHROOMS</text>

    <text class="info-strong" x="63" y="540" font-size="14">PRODUCT OF USA</text>
    <text class="info-regular" x="63" y="559" font-size="14">Keep Refridgerated</text>
    <text class="info-strong" x="63" y="578" font-size="14">NET WT.</text>
    <rect class="weight-box" x="197" y="524" width="165" height="60" fill="var(--paper)" stroke="var(--ink)" stroke-width="1.5"/>

    <text class="website" x="214" y="611" font-size="13" text-anchor="middle" textLength="250" lengthAdjust="spacing">www.yourcompanywebsite.com</text>
  </svg>

  <!-- Label option two: straight white panel -->
  <svg class="label label--two" viewBox="0 0 429 641" aria-label="Fresh produce mushrooms label, option two">
    <defs>
      <linearGradient id="field-fade" x1="0" y1="0" x2="0" y2="1">
        <stop offset="0" stop-color="var(--brand-red)"/>
        <stop offset="0.6" stop-color="var(--brand-red-deep)"/>
        <stop offset="1" stop-color="var(--brand-red)"/>
      </linearGradient>
    </defs>
    <rect class="label-frame" x="0" y="0" width="429" height="641" fill="var(--ink)"/>
    <rect class="label-field" x="7" y="7" width="415" height="627" fill="url(#field-fade)"/>
    <rect class="label-panel" x="12" y="385" width="406" height="241" fill="var(--paper)"/>

    <circle class="logo-emblem" cx="214" cy="70" r="28" fill="var(--paper)" role="img" aria-label="Mushroom emblem of the brand"/>
    <text class="logo-small" x="214" y="165" font-size="62" text-anchor="middle" textLength="143" lengthAdjust="spacingAndGlyphs">YOUR</text>
    <text class="logo-big" x="214" y="270" font-size="130" text-anchor="middle" textLength="279" lengthAdjust="spacingAndGlyphs">LOGO</text>
    <text class="logo-sub" x="214" y="330" font-size="63" text-anchor="middle" textLength="282" lengthAdjust="spacingAndGlyphs">GOES HERE</text>

    <rect class="fresh-pill" x="133" y="361" width="162" height="42" rx="21" fill="var(--ink)" stroke="var(--paper)" stroke-width="3"/>
    <text class="fresh" x="214" y="396" font-size="38" text-anchor="middle" textLength="116" lengthAdjust="spacingAndGlyphs">FRESH</text>

    <text class="product-line" x="214" y="457" font-size="52" text-anchor="middle" textLength="201" lengthAdjust="spacingAndGlyphs">PRODUCE</text>
    <text class="product-name product-name--red" x="214" y="507" font-size="59" text-anchor="middle" textLength="327" lengthAdjust="spacingAndGlyphs">MUSHROOMS</text>

    <text class="info-strong" x="36" y="540" font-size="14">PRODUCT OF USA</text>
    <text class="info-regular" x="36" y="559" font-size="14">Keep Refridgerated</text>
    <text class="info-strong" x="36" y="578" font-size="14">NET WT.</text>
    <rect class="weight-box" x="232" y="520" width="167" height="64" fill="var(--paper)" stroke="var(--ink)" stroke-width="1.5"/>

    <text class="website" x="214" y="611" font-size="13" text-anchor="middle" textLength="251" lengthAdjust="spacing">www.yourcompanywebsite.com</text>
  </svg>
</main>
</body>
</html>
```